Cover for Small sparks Make Small Fires

Book Cover Request
Format: Print and electronic (Bookvale)
Book Title: Small Sparks Make Small Fires: Practical Roadmap for Momentum and Purpose
Author: R.K. Vandemeer
Description: This self-help book, written by me, a self-proclaimed nobody, is filled with actionable insights and proven strategies that can help anyone. It combines humor with a serious undertone to deliver practical advice without the typical "self-helpy" vibe.
Catchphrase for the Cover: "Go from Oh Shit to Crushing It!" (or something similar)
Style: I want the cover to reflect my personality—funny, yet serious when needed. I'm open to suggestions and would love to see a design that captures the essence of the book without being too typical of the self-help genre.
Additional Information: I've attached a rough draft of the Bookvale description for more context.
Thank you for your help!
Target Market(s)
Anyone. but id say over 25
Requirements
Nice to have
- Honestly im really at a loss. Im hoping the description will help guide you. I gues i would like it to satand out of course. Be diffrent....but i know how crazy that sounds because everyone wants that. Just give me soem ideas!

```html
<!DOCTYPE html>
<html lang="en">
<head>
<meta charset="utf-8">
<title>Small Sparks Make Small Fires — Book Cover</title>
<link rel="stylesheet" href="https://fonts.googleapis.com/css2?family=Antonio:wght@500;700&family=Kaushan+Script&family=Jost:wght@400&display=swap">
<style>
  :root {
    --stage: #4fbfae;
    --paper-light: #f6e2d0;
    --paper-mid: #ecc9b1;
    --paper-edge: #bf9a8c;
    --ink-black: #0c0c0c;
    --ink-teal: #0d6b5d;
    --ink-purple: #9a1ee6;
    --author-teal: #124d45;
    --photo-skin: #e8b89c;
    --photo-shirt: #f4ece6;
    --photo-stripe: #c2443a;
  }
  html, body {
    margin: 0;
    padding: 0;
    width: 1200px;
    height: 900px;
    overflow: hidden;
    background: var(--stage);
  }
  .stage {
    position: relative;
    width: 1200px;
    height: 900px;
  }
  .book-cover {
    position: absolute;
    left: 332px;
    top: 20px;
    width: 536px;
    height: 860px;
    display: block;
  }
  .author-name {
    font-family: "Antonio", "Arial Narrow", sans-serif;
    font-weight: 500;
    fill: var(--author-teal);
    letter-spacing: 4px;
  }
  .title-line {
    font-family: "Antonio", "Arial Narrow", sans-serif;
    font-weight: 700;
  }
  .title-line--black { fill: var(--ink-black); }
  .title-line--teal { fill: var(--ink-teal); }
  .title-connector {
    font-family: "Kaushan Script", cursive;
    fill: var(--ink-purple);
  }
  .subtitle {
    font-family: "Jost", "Futura", sans-serif;
    font-weight: 400;
    fill: var(--ink-black);
    text-transform: uppercase;
  }
</style>
</head>
<body>
<main class="stage">
  <svg class="book-cover" viewBox="0 0 705 1130" xmlns="http://www.w3.org/2000/svg" aria-labelledby="cover-title">
    <title id="cover-title">Small Sparks Make Small Fires: Practical Roadmap for Momentum and Purpose, by R.K. Vandemeer</title>
    <defs>
      <radialGradient id="paper-tone" cx="50%" cy="50%" r="70%">
        <stop offset="0%" stop-color="var(--paper-light)"/>
        <stop offset="65%" stop-color="var(--paper-mid)"/>
        <stop offset="100%" stop-color="var(--paper-edge)"/>
      </radialGradient>
      <linearGradient id="portrait-tone" x1="0" y1="0" x2="0" y2="1">
        <stop offset="0%" stop-color="var(--photo-skin)" stop-opacity="0.55"/>
        <stop offset="45%" stop-color="var(--photo-skin)" stop-opacity="0.5"/>
        <stop offset="60%" stop-color="var(--photo-shirt)" stop-opacity="0.7"/>
        <stop offset="85%" stop-color="var(--photo-stripe)" stop-opacity="0.25"/>
        <stop offset="100%" stop-color="var(--photo-shirt)" stop-opacity="0"/>
      </linearGradient>
    </defs>

    <rect class="cover-paper" x="0" y="0" width="705" height="1130" fill="url(#paper-tone)"/>

    <rect class="cover-portrait" x="318" y="252" width="387" height="630" fill="url(#portrait-tone)"
          role="img" aria-label="Photo of a man in a red and white striped shirt slapping his forehead in dismay"/>

    <text class="author-name" x="353" y="77" font-size="60" text-anchor="middle" textLength="270" lengthAdjust="spacingAndGlyphs">R.K. VANDEMEER</text>

    <text class="title-line title-line--black" x="43" y="287" font-size="240" textLength="520" lengthAdjust="spacingAndGlyphs">SMALL</text>
    <text class="title-line title-line--black" x="43" y="454" font-size="190" textLength="560" lengthAdjust="spacingAndGlyphs">SPARKS</text>

    <text class="title-connector" x="43" y="582" font-size="140" textLength="270" lengthAdjust="spacingAndGlyphs">make</text>

    <text class="title-line title-line--teal" x="43" y="777" font-size="220" textLength="555" lengthAdjust="spacingAndGlyphs">SMALL</text>
    <text class="title-line title-line--teal" x="43" y="984" font-size="236" textLength="585" lengthAdjust="spacingAndGlyphs">FIRES</text>

    <text class="subtitle" x="353" y="1047" font-size="34" text-anchor="middle" textLength="490" lengthAdjust="spacingAndGlyphs">Practical Roadmap for Momentum</text>
    <text class="subtitle" x="353" y="1090" font-size="34" text-anchor="middle">and Purpose</text>
  </svg>
</main>
</body>
</html>
```